New homepage and Product page - Meadow Vy

Reason: I have narrowed it done to 3 designers and just need to get the designs revised

Industry/Entity Type

Product

```html
<!DOCTYPE html>
<html lang="en">
<head>
<meta charset="utf-8">
<title>Meadow Vy — Home</title>
<link href="https://fonts.googleapis.com/css2?family=Lato:wght@400;700;900&display=swap" rel="stylesheet">
<style>
:root{
  --green-dark:#0f6b3c;
  --green:#8bc23f;
  --green-deep:#006838;
  --orange:#e57e2c;
  --red:#cc1c1f;
  --text-muted:#9a9a9a;
  --text-body:#6f8a63;
  --page:#f6f6f6;
  --white:#ffffff;
  --box-edge:#dcdcdc;
}
*{margin:0;padding:0;box-sizing:border-box}
html,body{width:1200px;height:1078px;overflow:hidden}
body{font-family:'Lato',sans-serif;background:var(--page);position:relative}
.header{position:absolute;left:0;top:0;width:1200px;height:91px;background:linear-gradient(#f4f4f4,#fff)}
.brand{position:absolute;left:158px;top:18px;font-weight:900;font-size:31px;color:var(--green-dark);letter-spacing:1px;display:flex;align-items:center;gap:10px}
.brand .dot{width:14px;height:14px;border-radius:50%;background:var(--green)}
.contact-bar{position:absolute;right:165px;top:9px;display:flex;gap:22px;font-size:11px;color:var(--text-muted)}
.contact-bar span{display:flex;align-items:center;gap:6px}
.nav{position:absolute;left:730px;top:47px;display:flex;height:44px}
.nav a{display:flex;align-items:center;padding:0 17px;font-weight:900;font-size:16px;color:var(--green-dark);text-decoration:none}
.nav a.active{background:var(--green);color:var(--white);border-radius:3px 3px 0 0;gap:6px}
.dropdown{position:absolute;left:0;top:91px;width:1200px;height:74px;background:var(--green);border-top:3px solid #7aae33}
.drop-item{position:absolute;top:3px;display:flex}
.drop-item .pack{width:93px;height:68px;background:linear-gradient(#fff 0 45%,#f2c200 45% 65%,#5a8a3a 65%)}
.drop-item .txt{margin-left:12px;padding-top:16px;color:var(--white)}
.drop-item h3{font-weight:400;font-size:17px}
.drop-item small{display:block;margin-top:4px;font-size:11px;letter-spacing:1px;color:#5f8f27}
.hero{position:absolute;left:0;top:165px;width:1200px;height:476px;background:linear-gradient(160deg,#dfe9b8 0%,#eaf4d9 45%,#d6f6ee 100%)}
.hero-photo{position:absolute;left:660px;top:0;width:450px;height:476px;background:radial-gradient(ellipse at 50% 40%,#f1dcc9 0%,#f6eee6 45%,rgba(255,255,255,0) 75%)}
.seal{position:absolute;left:223px;top:70px}
.hero-copy{position:absolute;left:378px;top:78px;width:380px}
.hero-copy .tag{font-size:15px;color:var(--green-dark)}
.hero-copy h1{font-weight:900;font-size:30px;color:var(--green-dark);margin-top:2px}
.hero-copy p{font-size:15px;line-height:21px;color:var(--text-body);margin-top:4px}
.card{position:absolute;top:543px;width:281px;height:369px;background:var(--white);text-align:center}
.card .box{width:118px;height:152px;margin:22px auto 0;border:1px solid var(--box-edge)}
.card h2{font-weight:400;font-size:18px;margin-top:10px}
.card p{text-align:left;font-size:11px;line-height:17px;color:var(--text-muted);padding:0 20px;margin-top:14px}
.card .btn{position:absolute;left:0;bottom:0;width:281px;height:33px;color:var(--white);font-weight:700;font-size:11px;letter-spacing:.5px;text-align:left;padding:10px 23px}
.grass{position:absolute;left:0;top:950px;width:1200px;height:128px}
.copyright{position:absolute;left:0;top:1057px;width:1200px;text-align:center;font-size:10px;color:var(--white)}
</style>
</head>
<body>
<header class="header">
  <div class="brand"><span>MEADOW VY</span><span class="dot"></span></div>
  <div class="contact-bar">
    <span><svg width="16" height="11"><rect x="1" y="1" width="14" height="9" fill="none" stroke="#8bc23f"/><path d="M1 1l7 5 7-5" fill="none" stroke="#8bc23f"/></svg>hello@meadowvy.com</span>
    <span><svg width="12" height="13"><path d="M3 1l2 3-1.5 1.5c1 2 2 3 4 4L9 8l3 2-2 2.5C5 12 1 7 1 3z" fill="#8bc23f"/></svg>+88 000 555 123</span>
  </div>
  <nav class="nav">
    <a href="#">HOME</a>
    <a href="#" class="active">PRODUCTS <svg width="10" height="7"><path d="M1 1l4 4 4-4" stroke="#fff" stroke-width="2" fill="none"/></svg></a>
    <a href="#">CONTACT</a>
  </nav>
</header>

<div class="dropdown">
  <div class="drop-item" style="left:161px"><div class="pack" role="img" aria-label="Green Coffee Bean package"></div><div class="txt"><h3>Green Coffee Bean</h3><small>VIEW DETAILS ➔</small></div></div>
  <div class="drop-item" style="left:449px"><div class="pack" role="img" aria-label="Garcinia Cambogia package"></div><div class="txt"><h3>Garcinia Cambogia</h3><small>VIEW DETAILS ➔</small></div></div>
  <div class="drop-item" style="left:751px"><div class="pack" role="img" aria-label="Raspberry Ketone package"></div><div class="txt"><h3>Raspberry Ketone</h3><small>VIEW DETAILS ➔</small></div></div>
</div>

<section class="hero">
  <div class="hero-photo" role="img" aria-label="Photo of a smiling woman in a white top"></div>
  <svg class="seal" width="140" height="140" viewBox="0 0 140 140"><circle cx="70" cy="70" r="68" fill="#0f6b3c"/><circle cx="70" cy="70" r="58" fill="#f3f3ee"/></svg>
  <div class="hero-copy">
    <div class="tag">Fresh From the Meadow, Every Day</div>
    <h1>A BRAND YOU CAN TRUST</h1>
    <p>New Meadow Vy is line of natural, high-quality, weight-loss supplements that are scientifically formulated for better efficacy!</p>
  </div>
</section>

<article class="card" style="left:159px">
  <div class="box" role="img" aria-label="Garcinia Cambogia bonus pack box" style="background:linear-gradient(#fff 0 40%,#e57e2c 40% 48%,#f2c200 48% 60%,#7a9a3a 60%)"></div>
  <h2 style="color:var(--orange)">Start Losing Weight Today!</h2>
  <p>Meadow Vy Garcinia Cambogia is made with 100% pure natural ingredients. Unlike other products, Meadow Vy Garcinia Cambogia is made with premium garcinia cambogia that supplies 60% HCA, which is the active weight-loss component of garcinia cambogia.</p>
  <div class="btn" style="background:var(--orange)">LEARN MORE ➔</div>
</article>
<article class="card" style="left:459px">
  <div class="box" role="img" aria-label="Green Coffee Bean bonus pack box" style="background:linear-gradient(#fff 0 40%,#006838 40% 48%,#f2c200 48% 60%,#5a8a3a 60%)"></div>
  <h2 style="color:var(--green-deep)">Effective Weight Loss</h2>
  <p>Meadow Vy Green Coffee Bean is made with 100% pure natural ingredients. Unlike other products, Meadow Vy Green Coffee Bean is made with premium green coffee bean that supplies 45% chlorogenic acid, which is the active weight-loss component of green coffee bean.</p>
  <div class="btn" style="background:var(--green-deep)">LEARN MORE ➔</div>
</article>
<article class="card" style="left:762px">
  <div class="box" role="img" aria-label="Raspberry Ketone bonus pack box" style="background:linear-gradient(#fff 0 40%,#cc1c1f 40% 48%,#f2c200 48% 60%,#b52a3a 60%)"></div>
  <h2 style="color:var(--red)">Natural Premium Green Tea</h2>
  <p>Meadow Vy Raspberry Ketone is made with 100% pure raspberry ketone along with natural premium green tea.</p>
  <div class="btn" style="background:var(--red)">LEARN MORE ➔</div>
</article>

<div class="grass" role="img" aria-label="Illustration of green grass" style="background:linear-gradient(rgba(139,194,63,0),#8bc23f 35%)"></div>
<div class="copyright">Copyright © 2014 All Rights Reserved by Meadow Vy</div>
</body>
</html>
```